3D Printing Website redesign

We are in the process of redesigning our website. Attached is an image of one of the proposed pages - "The Quotewheel". The idea with this page is that site visitors can get an indicative estimate of the cost of 3D Printing based on some provided metrics. When the user alters the metrics the price changes accordingly. We are looking for a design to support this page that will also be used across our site.

Industry/Entity Type

Printing

```html
<!DOCTYPE html>
<html lang="en">
<head>
<meta charset="utf-8">
<title>Layerworks Studio – The Quotewheel</title>
<link rel="stylesheet" href="https://fonts.googleapis.com/css2?family=Open+Sans:wght@400;600;700&family=Oswald:wght@400&family=Ubuntu:wght@500;700&display=swap">
<style>
:root{
  --brand-blue:#1f5597;
  --brand-blue-dark:#174a87;
  --calc-blue:#1e9be6;
  --calc-blue-light:#38aef0;
  --action-blue:#1577d6;
  --nav-active:#1a7bd0;
  --yellow:#fcc21a;
  --yellow-dark:#e8a90c;
  --orange:#e8751a;
  --grey-bar:#e6e6e6;
  --grey-panel:#f1f1f1;
  --grey-border:#d9d9d9;
  --text-dark:#333;
  --text-mid:#666;
  --white:#fff;
}
*{box-sizing:border-box;margin:0;padding:0}
html,body{width:1014px;height:1200px;overflow:hidden}
body{position:relative;background:var(--white);font-family:"Open Sans",Arial,sans-serif;color:var(--text-dark)}
.abs{position:absolute}

/* top bar */
.topbar{left:0;top:0;width:1014px;height:34px;background:var(--grey-bar);font-size:12px;color:var(--text-mid)}
.topbar .contact{left:128px;top:9px;display:flex;gap:22px;align-items:center}
.topbar .contact span{display:flex;align-items:center;gap:6px}
.topbar .account{left:712px;top:10px;font-size:11px;display:flex;gap:12px}
.topbar .lang{left:818px;top:7px;width:40px;height:20px;background:var(--white);border:1px solid #ccc;border-radius:2px}
.topbar .lang i{position:absolute;left:3px;top:3px;width:22px;height:12px;background:var(--brand-blue)}
.topbar .search{left:866px;top:6px;width:22px;height:22px;background:var(--white);border:1px solid #ccc;border-radius:2px}

/* blue band */
.band{left:0;top:34px;width:1014px;height:366px;background:var(--brand-blue)}

/* main card */
.card{left:92px;top:44px;width:830px;height:555px;background:linear-gradient(#fff,#f3f3f3 70%,#fff);border-radius:4px;box-shadow:0 4px 16px rgba(0,0,0,.18)}
.brand{left:128px;top:66px;display:flex;align-items:center;gap:8px;font-family:"Ubuntu",sans-serif;font-weight:700;font-size:16px;color:var(--brand-blue)}
.brand i{width:36px;height:36px;border-radius:50%;background:var(--brand-blue)}
.nav{left:335px;top:70px;width:555px;display:flex;justify-content:space-between;font-family:"Oswald",sans-serif;font-size:12.5px;color:#333;text-transform:uppercase}
.nav a{padding:0 6px;height:21px;line-height:21px;color:inherit;text-decoration:none;white-space:nowrap}
.nav a:last-child{padding-right:0}
.nav a.active{background:var(--nav-active);color:var(--white);border-radius:2px}
.rule{left:119px;top:127px;width:776px;height:1px;background:#e4e4e4}

.quote-btn{left:392px;top:157px;width:228px;height:34px;border-radius:17px;background:linear-gradient(#2a8ee6,var(--action-blue));box-shadow:0 0 0 4px #e8eef5;color:var(--white);font-weight:700;font-size:13px;display:flex;align-items:center;justify-content:center;gap:12px}
.or{left:0;width:1014px;top:200px;text-align:center;font-size:22px;font-weight:600;color:#aaa}

/* quote calculator */
.calc-frame{left:118px;top:239px;width:777px;height:351px;border:1px solid #ddd;border-radius:5px;background:var(--white)}
.calc{left:127px;top:248px;width:760px;height:333px;border-radius:4px;background:linear-gradient(160deg,var(--calc-blue) 55%,var(--calc-blue-light));overflow:hidden}
.mode{left:151px;width:153px;height:42px;border-radius:4px;background:linear-gradient(#fdd14a,var(--yellow));border-bottom:2px solid var(--yellow-dark);color:#5a4200;font-family:"Ubuntu",sans-serif;font-weight:500;font-size:17px;display:flex;align-items:center;justify-content:space-between;padding:0 12px 0 18px}
.tag{left:343px;width:270px;text-align:center}
.tag span{display:inline-block;background:#e9f4fc;color:#333;font-size:11px;font-weight:700;padding:2px 12px;border-radius:4px}
.track{left:343px;width:270px;height:7px;border-radius:4px;background:var(--brand-blue-dark)}
.track b{position:absolute;left:0;top:0;height:7px;border-radius:4px;background:var(--orange)}
.track i{position:absolute;top:-4px;width:15px;height:15px;border-radius:50%;background:var(--yellow);border:2px solid #c98a00}
.ends{left:343px;top:313px;width:270px;display:flex;justify-content:space-between;color:var(--white);font-size:11px;font-weight:700}
.select{left:345px;top:517px;width:267px;height:33px;border-radius:4px;background:#1a5fa8;border:1px solid #16508f}
.select i{position:absolute;right:0;top:0;width:40px;height:31px;background:#17529a;border-radius:0 4px 4px 0}
.price{left:717px;top:321px;width:128px;height:128px;border-radius:50%;background:var(--brand-blue);box-shadow:0 0 0 2px #2a70bd;color:var(--white);font-size:42px;font-weight:400;display:flex;align-items:center;justify-content:center}
.total{left:682px;top:472px;width:200px;text-align:center;color:var(--white);font-size:12px;font-weight:700}

/* enquiry form */
.form{left:119px;top:630px;width:776px;height:254px;border:1px solid var(--grey-border);border-radius:3px;background:var(--grey-panel)}
.form h2{position:absolute;left:0;top:0;width:774px;height:42px;background:#e3e3e3;padding:12px 23px;font-family:"Ubuntu",sans-serif;font-weight:500;font-size:16px;color:#333}
.field{background:var(--white);border:1px solid #ccc;border-radius:3px;box-shadow:0 0 0 2px #f7f7f7;font-size:10px;color:#888;padding:7px 9px}
.captcha{left:144px;top:822px;width:62px;height:35px;background:#111;border:2px solid #555;color:var(--white);font-weight:700;font-size:13px;display:flex;align-items:center;justify-content:center}
.agree{left:350px;top:841px;display:flex;align-items:center;gap:8px;font-size:10px;color:#1c5ca8}
.agree i{width:11px;height:11px;border:1px solid #999;background:var(--white)}
.send{left:806px;top:832px;width:63px;height:22px;border-radius:11px;background:var(--action-blue);color:var(--white);font-weight:700;font-size:11px;display:flex;align-items:center;justify-content:center;gap:6px}

.intro{left:119px;top:922px;font-size:10.5px;color:#666}

/* footer */
.footer{left:0;top:944px;width:1014px;height:220px;background:radial-gradient(ellipse at 20% 10%,#2a64a8,var(--brand-blue) 60%)}
.fcol{color:var(--white)}
.fcol h3{font-family:"Ubuntu",sans-serif;font-weight:500;font-size:15px;margin-bottom:6px}
.fcol li{list-style:none;font-size:10.5px;color:#d6e2f0;line-height:21.5px;padding-left:16px;position:relative}
.fcol li::before{content:"";position:absolute;left:2px;top:9px;width:4px;height:4px;background:#7fa3cc;transform:rotate(45deg)}
.fcol h3.sub{margin-top:20px}
.newsletter{left:654px;top:968px;width:232px;height:142px;background:#f0f0f0;border:1px solid #ccc;border-radius:3px;padding:12px 18px}
.newsletter h4{font-family:"Ubuntu",sans-serif;font-weight:500;font-size:14px;color:#333}
.newsletter p{font-size:10px;color:#666;margin-top:3px}
.newsletter .field{margin-top:12px;height:28px}
.submit{left:139px;top:102px;width:77px;height:23px;border-radius:11px;background:var(--action-blue);color:var(--white);font-weight:700;font-size:11px;display:flex;align-items:center;justify-content:center;gap:6px}

.bottombar{left:0;top:1164px;width:1014px;height:36px;background:var(--grey-bar);font-size:10.5px;color:#555}
.bottombar .copy{left:119px;top:11px}
.bottombar .admin{left:357px;top:11px;color:#1c5ca8}
.social{left:786px;top:9px;display:flex;gap:8px}
.social i{width:19px;height:19px;border-radius:50%;background:var(--brand-blue)}
.social i:last-child{background:#c8402f}
</style>
</head>
<body>

<div class="abs topbar">
  <div class="abs contact">
    <span><svg width="12" height="12" viewBox="0 0 12 12"><path d="M2 1h3l1 3-2 1a7 7 0 0 0 3 3l1-2 3 1v3a1 1 0 0 1-1 1A10 10 0 0 1 1 2a1 1 0 0 1 1-1z" fill="#777"/></svg>1300 - 555 - 010</span>
    <span><svg width="13" height="10" viewBox="0 0 13 10"><rect x=".5" y=".5" width="12" height="9" fill="none" stroke="#777"/><path d="M.5.5l6 5 6-5" fill="none" stroke="#777"/></svg>hello@layerworks.example</span>
  </div>
  <div class="abs account"><span>LOGIN</span><span>REGISTER</span></div>
  <div class="abs lang"><i></i></div>
  <div class="abs search"><svg width="20" height="20" viewBox="0 0 20 20"><circle cx="9" cy="9" r="4" fill="none" stroke="#555" stroke-width="2"/><path d="M12 12l4 4" stroke="#555" stroke-width="2"/></svg></div>
</div>

<div class="abs band"></div>

<div class="abs card"></div>
<div class="abs brand"><i></i>Layerworks Studio</div>
<nav class="abs nav">
  <a class="active">Home</a><a>Shop</a><a>Printing &amp; Quotes</a><a>Printing Cafe</a><a>Materials</a><a>Gallery</a><a>Training</a><a>About Us</a><a>Blog</a>
</nav>
<div class="abs rule"></div>

<div class="abs quote-btn">GET AN INSTANT QUOTE
  <svg width="12" height="12" viewBox="0 0 12 12"><path d="M0 3h6V0l6 6-6 6V9H0z" fill="#fff"/></svg>
</div>
<div class="abs or">or</div>

<div class="abs calc-frame"></div>
<section class="abs calc" aria-label="The Quotewheel"></section>

<div class="abs mode" style="top:281px">Print
  <svg width="24" height="22" viewBox="0 0 24 22"><rect x="6" y="1" width="12" height="6" fill="none" stroke="#5a4200" stroke-width="2"/><rect x="1" y="7" width="22" height="9" rx="2" fill="none" stroke="#5a4200" stroke-width="2"/><rect x="6" y="13" width="12" height="8" fill="#fdd14a" stroke="#5a4200" stroke-width="2"/></svg></div>
<div class="abs mode" style="top:340px">Scan
  <svg width="24" height="22" viewBox="0 0 24 22"><path d="M2 18h20l-2-5H4z" fill="#5a4200"/><path d="M6 12L18 2" stroke="#5a4200" stroke-width="3"/></svg></div>
<div class="abs mode" style="top:397px">Design
  <svg width="24" height="22" viewBox="0 0 24 22"><rect x="2" y="4" width="16" height="16" fill="none" stroke="#5a4200" stroke-width="2"/><path d="M9 14l2-4 9-9 2 2-9 9z" fill="#5a4200"/></svg></div>

<div class="abs tag" style="top:265px"><span>SHAPE</span></div>
<div class="abs track" style="top:301px"><b style="width:112px"></b><i style="left:101px"></i></div>
<div class="abs ends"><span>SQUARE</span><span>CIRCULAR</span></div>
<div class="abs tag" style="top:333px"><span>SIZE</span></div>
<div class="abs track" style="top:368px"><b style="width:158px"></b><i style="left:148px"></i></div>
<div class="abs tag" style="top:408px"><span>VOLUME</span></div>
<div class="abs track" style="top:445px"><b style="width:112px"></b><i style="left:101px"></i></div>
<div class="abs tag" style="top:482px"><span>MATERIAL</span></div>
<div class="abs select"><i><svg width="40" height="31" viewBox="0 0 40 31"><path d="M14 12h12l-6 9z" fill="#3d8ad6"/></svg></i></div>

<div class="abs price">$36</div>
<div class="abs total">QUOTEWHEEL TOTAL: $36</div>

<section class="abs form">
  <h2>Lorem Ipsum is simply dummy text</h2>
</section>
<div class="abs field" style="left:145px;top:698px;width:226px;height:27px">Full Name...</div>
<div class="abs field" style="left:394px;top:698px;width:225px;height:27px">Email Address...</div>
<div class="abs field" style="left:642px;top:698px;width:224px;height:27px">Phone Number...</div>
<div class="abs field" style="left:144px;top:744px;width:724px;height:59px">Message...</div>
<div class="abs captcha">xWuab</div>
<div class="abs field" style="left:224px;top:830px;width:101px;height:27px">Enter the code...</div>
<div class="abs agree"><i></i>I agree to the Terms of Services and Privacy Policy</div>
<div class="abs send">SEND <svg width="8" height="8" viewBox="0 0 12 12"><path d="M0 3h6V0l6 6-6 6V9H0z" fill="#fff"/></svg></div>

<p class="abs intro">Lorem Ipsum is simply dummy text of the printing and typesetting industry. Lorem Ipsum has been the industry's...</p>

<footer class="abs footer"></footer>
<div class="abs fcol" style="left:127px;top:964px">
  <h3>Printing</h3><ul><li>Quote</li><li>Technologies</li></ul>
  <h3 class="sub">Printers</h3><ul><li>Machines for sale</li><li>Machines to rent</li><li>Servicing</li><li>Buy Materials</li></ul>
</div>
<div class="abs fcol" style="left:289px;top:964px">
  <h3>Materials</h3><ul><li>Overview</li><li>Plastic</li><li>Powder</li><li>High-Detail Resin</li><li>Nylon</li><li>Wood</li><li>Rubber</li></ul>
</div>
<div class="abs fcol" style="left:452px;top:964px">
  <h3>Training</h3><ul><li>Sydney 3D Printers Meetup</li><li>Studio Workshops</li></ul>
  <h3 class="sub">Franchise</h3><ul><li>Franchise Opportunity</li></ul>
</div>
<div class="abs newsletter">
  <h4>Newsletter</h4>
  <p>Want to receive our Newsletter?</p>
  <div class="field">Enter your email address...</div>
  <div class="abs submit">SUBMIT <svg width="8" height="8" viewBox="0 0 12 12"><path d="M0 3h6V0l6 6-6 6V9H0z" fill="#fff"/></svg></div>
</div>

<div class="abs bottombar">
  <span class="abs copy">© 2013 Layerworks Studio. All rights reserved.</span>
  <span class="abs admin">Admin Log In</span>
  <div class="abs social"><i></i><i></i><i></i><i></i></div>
</div>

</body>
</html>
```